Window Advertisment for Rentals Company

I own a property rental company in Cyprus and I am looking for an eye catching design to place in my window to attract passers by.

Please check the attachment for more details.

Ad size to be 309cm x 204cm landscape

The font of the logo is velocity

Target Market(s)

Property Owners

Industry/Entity Type

It Company

Requirements
Must have
• The colours from my logo and be eye catching and make passers by take notice

```html
<!DOCTYPE html>
<html lang="en">
<head>
<meta charset="utf-8">
<title>Sunhaven Stays – Window Advert</title>
<link rel="stylesheet" href="https://fonts.googleapis.com/css2?family=Alfa+Slab+One&family=Bowlby+One&family=Cabin:wght@600;700&display=swap">
<style>
  :root {
    --sun-yellow: #fff200;
    --ink: #0a0a0a;
    --band-orange: #f37021;
    --paper: #ffffff;
    --brand-orange: #f7941d;
  }
  html, body {
    margin: 0;
    padding: 0;
    overflow: hidden;
    background: var(--paper);
  }
  .advert {
    display: block;
    width: 1200px;
    height: 792px;
  }
  .backdrop { fill: var(--sun-yellow); }
  .artwork { fill: var(--ink); }
  .call-band { fill: var(--band-orange); }
  .corner-panel { fill: var(--paper); }
  .steps { fill: var(--ink); }
  .headline {
    font-family: "Alfa Slab One", Georgia, serif;
    font-size: 38px;
    fill: var(--ink);
  }
  .call-label, .call-number {
    font-family: "Bowlby One", Impact, sans-serif;
    fill: var(--ink);
  }
  .call-label { font-size: 46px; }
  .call-number { font-size: 78px; }
  .phone-icon { fill: var(--ink); }
  .benefits {
    font-family: "Cabin", Arial, sans-serif;
    font-weight: 600;
    font-size: 21px;
    fill: var(--paper);
    letter-spacing: 0.5px;
  }
  .brand-name {
    font-family: "Cabin", Arial, sans-serif;
    font-weight: 600;
    font-size: 38px;
    fill: var(--brand-orange);
  }
  .brand-dot { fill: var(--brand-orange); }
  .web-address {
    font-family: "Cabin", Arial, sans-serif;
    font-weight: 700;
    font-size: 18.5px;
    fill: var(--ink);
    letter-spacing: 0.3px;
  }
</style>
</head>
<body>
<svg class="advert" viewBox="0 0 1200 792" xmlns="http://www.w3.org/2000/svg">
  <rect class="backdrop" x="0" y="0" width="1200" height="792"/>

  <!-- apartment tower illustration -->
  <rect class="artwork" x="18" y="34" width="164" height="426" role="img" aria-label="Silhouette illustration of a tall apartment tower"/>

  <!-- house illustrations -->
  <rect class="artwork" x="250" y="250" width="222" height="144" role="img" aria-label="Silhouette illustration of a two-storey villa"/>
  <rect class="artwork" x="556" y="282" width="282" height="112" role="img" aria-label="Silhouette illustration of a bungalow with garage"/>
  <rect class="artwork" x="926" y="258" width="164" height="140" role="img" aria-label="Silhouette illustration of a small house with chimney"/>

  <!-- headline -->
  <text class="headline" x="210" y="138" textLength="950" lengthAdjust="spacingAndGlyphs">WE ARE LOOKING FOR VILLAS AND APARTMENTS</text>
  <text class="headline" x="210" y="220" textLength="950" lengthAdjust="spacingAndGlyphs">TO FULFILL OUR GROWING DEMAND OF RENTALS</text>

  <!-- diagonal call band and white corner -->
  <polygon class="call-band" points="1200,340 1200,456 528,792 237,792"/>
  <polygon class="corner-panel" points="1200,456 1200,792 528,792"/>

  <!-- fence illustration -->
  <rect class="artwork" x="0" y="486" width="392" height="38" role="img" aria-label="Silhouette illustration of a picket fence"/>

  <!-- stepped black base -->
  <polygon class="steps" points="0,524 392,524 392,526 420,526 420,544 444,544 444,560 472,560 472,578 500,578 500,596 528,596 528,612 556,612 804,792 0,792"/>

  <!-- benefits -->
  <g class="benefits" text-anchor="middle">
    <text x="307" y="582">LOW COMMISSIONS</text>
    <text x="307" y="626">QUICK PAYOUTS</text>
    <text x="307" y="670">FREE ADVERTISING</text>
    <text x="307" y="714">CONNECT WITH OVER 35 LEADING WEBSITES</text>
    <text x="307" y="758">BE SEEN BY 100+ MILLION TRAVELLERS PER MONTH</text>
  </g>

  <!-- call to action -->
  <g transform="rotate(-27 680 560)">
    <text class="call-label" x="545" y="578">Call Now</text>
  </g>
  <g class="phone-icon" transform="translate(726 636) rotate(-27)">
    <path d="M-40,-14 Q-40,-32 0,-32 Q40,-32 40,-14 L40,-6 L22,-6 L22,-16 L-22,-16 L-22,-6 L-40,-6 Z"/>
    <path d="M-26,-4 L26,-4 L36,30 L-36,30 Z"/>
    <circle cx="0" cy="12" r="12" fill="var(--band-orange)"/>
    <circle cx="0" cy="12" r="6"/>
  </g>
  <g transform="rotate(-27 975 520)">
    <text class="call-number" x="975" y="548" text-anchor="middle">24 555019</text>
  </g>

  <!-- brand -->
  <circle class="brand-dot" cx="900" cy="694" r="10"/>
  <text class="brand-name" x="920" y="707">sunhaven stays</text>
  <text class="web-address" x="1000" y="768" text-anchor="middle">WWW.SUNHAVENSTAYSCY.COM</text>
</svg>
</body>
</html>
```